Letter Head- Window Cleaning Industry

Need a letter head for 'Fernbrook Window Cleaning'. We provide a premium residential & commercial window cleaning service to Melbourne and surrounding suburbs.
Would like a design similar to the flyer, logo and uniform attached. The final design should communicate trust and quality.
Address is 1204/58 Haldane St, Southmere Victoria 3141. The rest of the information is on the flyer.
*Please note the Phone number on the uniform designs is incorrect.

Thank-you very much!

Industry/Entity Type

Window Cleaning

```html
<!DOCTYPE html>
<html lang="en">
<head>
<meta charset="utf-8">
<title>Fernbrook Window Cleaning – Stationery Set</title>
<link href="https://fonts.googleapis.com/css2?family=Open+Sans:wght@400;600;700;800&family=Tinos&display=swap" rel="stylesheet">
<style>
:root{
  --backdrop:#e3e3e3;
  --paper:#ffffff;
  --orange:#f7931e;
  --ink:#111111;
  --text:#3a3a3a;
  --muted:#777777;
  --cell:#ececec;
  --skyline:#d9d9d9;
}
*{box-sizing:border-box;margin:0;padding:0}
html,body{width:1200px;height:548px;overflow:hidden}
body{background:var(--backdrop);font-family:"Open Sans",Arial,sans-serif;color:var(--text);position:relative}
.sheet{position:absolute;background:var(--paper);box-shadow:3px 4px 7px rgba(0,0,0,.28);overflow:hidden}

/* envelope back */
.envelope-back{left:48px;top:76px;width:365px;height:177px}
.envelope-flap{position:absolute;left:0;top:0;width:100%;height:59px;background:var(--orange);border-radius:0 0 16px 16px}

/* envelope front */
.envelope-front{left:48px;top:288px;width:365px;height:177px}
.envelope-front .brand{left:18px;top:18px;width:110px;height:64px}
.envelope-address{position:absolute;left:18px;top:95px;font-size:8.5px;font-weight:700;color:var(--ink);line-height:12px}
.swoosh{position:absolute;left:0;bottom:0;width:100%}

/* brand block */
.brand{position:absolute;display:flex;flex-direction:column;align-items:center;justify-content:center;gap:4px}
.brand-mark{width:12px;height:12px;background:var(--ink)}
.brand-name{font-weight:800;color:var(--ink);text-align:center;text-transform:uppercase;line-height:1.05}

/* letterhead & fax */
.letterhead{left:438px;top:27px;width:339px;height:480px}
.fax{left:812px;top:30px;width:338px;height:482px}
.letterhead .brand{left:95px;top:16px;width:150px;height:80px}
.fax .brand{left:105px;top:12px;width:130px;height:70px}
.brand-name.large{font-size:15px}
.brand-name.medium{font-size:13px}
.brand-name.small{font-size:10px}

.recipient{position:absolute;left:26px;top:105px;font-size:6px;line-height:7.4px;color:var(--text)}
.body-copy{position:absolute;font-size:5.6px;line-height:7.6px;color:var(--text);text-align:justify}
.body-copy p{margin-bottom:6px}
.body-copy p.serif{font-family:"Tinos","Times New Roman",serif;font-size:5.9px;color:#555}
.letterhead .body-copy{left:26px;top:143px;width:285px}
.fax .body-copy{left:22px;top:202px;width:286px}

.signature{position:absolute;width:62px;height:26px;border-radius:3px;background:linear-gradient(90deg,#ececec,#f6f6f6)}
.letterhead .signature{left:26px;top:358px}
.fax .signature{left:28px;top:363px}

.skyline{position:absolute;height:60px;background:linear-gradient(180deg,rgba(217,217,217,.2),var(--skyline))}
.letterhead .skyline{left:20px;width:300px;top:392px}
.fax .skyline{left:20px;width:300px;top:390px}

.contacts{position:absolute;font-size:8.2px;color:#333;line-height:11.5px;list-style:none}
.contacts li{display:flex;align-items:center;gap:4px}
.contacts svg{width:6px;height:6px;flex:none}
.letterhead .contacts.left{left:28px;top:407px}
.letterhead .contacts.right{left:211px;top:413px}
.fax .contacts.left{left:28px;top:407px}
.fax .contacts.right{left:210px;top:412px}

.footer-address{position:absolute;left:0;bottom:7px;width:100%;text-align:center;color:#fff;font-size:7.6px;font-weight:700}

/* fax table */
.fax-table{position:absolute;left:22px;top:94px;width:293px;border-collapse:separate;border-spacing:1px;font-size:5.4px;font-weight:600;color:#333}
.fax-table td{background:var(--cell);height:14.6px;padding-left:5px}
.fax-table td.value{width:104px}
.fax-table td.label{width:38px}
.fax-options{position:absolute;left:23px;top:163px;width:295px;display:flex;justify-content:space-between;font-size:5.1px;font-weight:600;color:#333}
.fax-options span{display:flex;align-items:center;gap:3px}
.fax-options i{width:6px;height:6px;border:0.7px solid #777;display:inline-block}
</style>
</head>
<body>

<!-- Envelope, back -->
<div class="sheet envelope-back">
  <div class="envelope-flap"></div>
</div>

<!-- Envelope, front -->
<div class="sheet envelope-front">
  <div class="brand">
    <span class="brand-mark"></span>
    <span class="brand-name small">Fernbrook<br>Window Cleaning</span>
  </div>
  <p class="envelope-address">2207 Parkline Way,<br>Rivergate, CA 95820</p>
  <svg class="swoosh" viewBox="0 0 365 60" width="365" height="60" preserveAspectRatio="none" aria-hidden="true">
    <path d="M0 30 C60 14 150 28 220 30 C285 32 330 20 365 2 L365 16 C320 38 270 46 200 44 C130 42 60 36 0 46 Z" fill="var(--ink)"/>
    <path d="M0 48 C70 38 140 46 210 48 C280 50 330 34 365 20 L365 60 L0 60 Z" fill="var(--orange)"/>
  </svg>
</div>

<!-- Letterhead -->
<div class="sheet letterhead">
  <div class="brand">
    <span class="brand-mark"></span>
    <span class="brand-name large">Fernbrook<br>Window Cleaning</span>
  </div>

  <p class="recipient">Lpsum, lorem<br>dolor sit amet<br>Lorem, dummy text</p>

  <div class="body-copy">
    <p>Lorem ipsum dolor sit amet, consetetur sadipscing elitr, sed diam nonumy eirmod tempor invidunt ut labore et dolore magna aliquyam erat, sed diam voluptua. At vero eos et accusam et justo duo dolores et ea rebum. Stet clita kasd gubergren, no sea takimata sanctus est Lorem ipsum dolor sit.</p>
    <p>Lorem ipsum dolor sit amet, consetetur sadipscing elitr, sed diam nonumy eirmod tempor invidunt ut labore et dolore magna aliquyam erat, sed diam voluptua. At vero eos et accusam et justo duo dolores et ea rebum. Stet clita kasd gubergren, no sea takimata sanctus est Lorem ipsum dolor sit. Lorem ipsum dolor sit amet, consetetur sadipscing elitr, sed diam nonumy eirmod tempor invidunt ut labore et dolore magna aliquyam erat, sed diam voluptua. At vero eos et accusam et justo duo dolores et ea rebum. Stet clita kasd gubergren, no sea takimata sanctus est Lorem ipsum dolor sit.</p>
    <p class="serif">Duis autem vel eum iriure dolor in hendrerit in vulputate velit esse molestie consequat, vel illum dolore eu feugiat nulla facilisis at vero eros et accumsan et iusto odio dignissim qui blandit praesent luptatum zzril delenit augue duis dolore te feugait nulla facilisi. Lorem ipsum dolor sit amet, consectetuer adipiscing elit, sed diam nonummy nibh euismod tincidunt ut laoreet dolore magna aliquam erat volutpat.</p>
    <p class="serif">Ut wisi enim ad minim veniam, quis nostrud exerci tation ullamcorper suscipit lobortis nisl ut aliquip ex ea commodo consequat. Duis autem vel eum iriure dolor in hendrerit in vulputate velit esse molestie consequat, vel illum dolore eu feugiat nulla facilisis at vero eros et accumsan et iusto odio dignissim qui blandit praesent luptatum zzril delenit augue duis dolore te feugait nulla facilisi.</p>
  </div>

  <div class="signature" role="img" aria-label="Handwritten signature of Jane Hollis"></div>
  <div class="skyline" role="img" aria-label="Faint city skyline silhouette"></div>

  <ul class="contacts left">
    <li><svg viewBox="0 0 6 6"><path d="M1 0.5 L2.3 0.5 L2.6 2 L1.9 2.5 Q2.6 3.7 3.6 4.1 L4.1 3.4 L5.5 3.7 L5.5 5 Q2.5 5.2 1 0.5 Z" fill="var(--orange)"/></svg>(555) 210-4418</li>
    <li><svg viewBox="0 0 6 6"><rect x="0.5" y="1.5" width="5" height="3.5" fill="var(--orange)"/><rect x="1.5" y="0.5" width="3" height="1" fill="var(--orange)"/></svg>(555) 210-4419</li>
    <li><svg viewBox="0 0 6 6"><rect x="1.5" y="0.3" width="3" height="5.4" rx="0.6" fill="none" stroke="var(--orange)" stroke-width="0.8"/></svg>(555) 388-7150</li>
  </ul>
  <ul class="contacts right">
    <li><svg viewBox="0 0 6 6"><rect x="0.3" y="1" width="5.4" height="4" fill="var(--orange)"/><path d="M0.3 1 L3 3.2 L5.7 1" stroke="#fff" stroke-width="0.6" fill="none"/></svg>hello@fernbrookwc.com</li>
    <li><svg viewBox="0 0 6 6"><circle cx="3" cy="3" r="2.6" fill="var(--orange)"/><path d="M0.4 3 H5.6 M3 0.4 V5.6" stroke="#fff" stroke-width="0.5"/></svg>www.fernbrookwc.com</li>
  </ul>

  <svg class="swoosh" viewBox="0 0 339 42" width="339" height="42" preserveAspectRatio="none" aria-hidden="true">
    <path d="M0 14 C80 4 180 10 250 12 C300 13 325 6 339 0 L339 12 C300 24 240 26 170 24 C100 22 40 20 0 24 Z" fill="var(--ink)"/>
    <path d="M0 24 C60 20 140 26 200 26 C270 26 310 20 339 14 L339 42 L0 42 Z" fill="var(--orange)"/>
  </svg>
  <p class="footer-address">2207 Parkline Way, Rivergate, CA 95820</p>
</div>

<!-- Fax sheet -->
<div class="sheet fax">
  <div class="brand">
    <span class="brand-mark"></span>
    <span class="brand-name medium">Fernbrook<br>Window Cleaning</span>
  </div>

  <table class="fax-table">
    <tr><td class="label">To</td><td class="value"></td><td class="label">From</td><td class="value"></td></tr>
    <tr><td class="label">FAX</td><td class="value"></td><td class="label">Pages</td><td class="value"></td></tr>
    <tr><td class="label">Phone</td><td class="value"></td><td class="label">Date</td><td class="value"></td></tr>
    <tr><td class="label">Re</td><td class="value"></td><td class="label">CC</td><td class="value"></td></tr>
  </table>

  <div class="fax-options">
    <span><i></i>Urgent</span>
    <span><i></i>For Review</span>
    <span><i></i>Please comment</span>
    <span><i></i>Please reply</span>
    <span><i></i>Please recycle</span>
  </div>

  <div class="body-copy">
    <p>Lorem ipsum dolor sit amet, consetetur sadipscing elitr, sed diam nonumy eirmod tempor invidunt ut labore et dolore magna aliquyam erat, sed diam voluptua. At vero eos et accusam et justo duo dolores et ea rebum. Stet clita kasd gubergren, no sea takimata sanctus est Lorem ipsum dolor sit.</p>
    <p>Lorem ipsum dolor sit amet, consetetur sadipscing elitr, sed diam nonumy eirmod tempor invidunt ut labore et dolore magna aliquyam erat, sed diam voluptua. At vero eos et accusam et justo duo dolores et ea rebum. Stet clita kasd gubergren, no sea takimata sanctus est Lorem ipsum dolor sit. Lorem ipsum dolor sit amet, consetetur sadipscing elitr, sed diam nonumy eirmod tempor invidunt ut labore et dolore magna aliquyam erat, sed diam voluptua. At vero eos et accusam et justo duo dolores et ea rebum. Stet clita kasd gubergren, no sea takimata sanctus est Lorem ipsum dolor sit.</p>
    <p class="serif">Duis autem vel eum iriure dolor in hendrerit in vulputate velit esse molestie consequat, vel illum dolore eu feugiat nulla facilisis at vero eros et accumsan et iusto odio dignissim qui blandit praesent luptatum zzril delenit augue duis dolore te feugait nulla facilisi. Lorem ipsum dolor sit amet, consectetuer adipiscing elit, sed diam nonummy nibh euismod tincidunt ut laoreet dolore magna aliquam erat volutpat.</p>
  </div>

  <div class="signature" role="img" aria-label="Handwritten signature of Jane Hollis"></div>
  <div class="skyline" role="img" aria-label="Faint city skyline silhouette"></div>

  <ul class="contacts left">
    <li><svg viewBox="0 0 6 6"><path d="M1 0.5 L2.3 0.5 L2.6 2 L1.9 2.5 Q2.6 3.7 3.6 4.1 L4.1 3.4 L5.5 3.7 L5.5 5 Q2.5 5.2 1 0.5 Z" fill="var(--orange)"/></svg>(555) 210-4418</li>
    <li><svg viewBox="0 0 6 6"><rect x="0.5" y="1.5" width="5" height="3.5" fill="var(--orange)"/><rect x="1.5" y="0.5" width="3" height="1" fill="var(--orange)"/></svg>(555) 210-4419</li>
    <li><svg viewBox="0 0 6 6"><rect x="1.5" y="0.3" width="3" height="5.4" rx="0.6" fill="none" stroke="var(--orange)" stroke-width="0.8"/></svg>(555) 388-7150</li>
  </ul>
  <ul class="contacts right">
    <li><svg viewBox="0 0 6 6"><rect x="0.3" y="1" width="5.4" height="4" fill="var(--orange)"/><path d="M0.3 1 L3 3.2 L5.7 1" stroke="#fff" stroke-width="0.6" fill="none"/></svg>hello@fernbrookwc.com</li>
    <li><svg viewBox="0 0 6 6"><circle cx="3" cy="3" r="2.6" fill="var(--orange)"/><path d="M0.4 3 H5.6 M3 0.4 V5.6" stroke="#fff" stroke-width="0.5"/></svg>www.fernbrookwc.com</li>
  </ul>

  <svg class="swoosh" viewBox="0 0 338 42" width="338" height="42" preserveAspectRatio="none" aria-hidden="true">
    <path d="M0 14 C80 4 180 10 250 12 C300 13 325 6 338 0 L338 12 C300 24 240 26 170 24 C100 22 40 20 0 24 Z" fill="var(--ink)"/>
    <path d="M0 24 C60 20 140 26 200 26 C270 26 310 20 338 14 L338 42 L0 42 Z" fill="var(--orange)"/>
  </svg>
  <p class="footer-address">2207 Parkline Way, Rivergate, CA 95820</p>
</div>

</body>
</html>
```